Business Card Design Project

Name: Kunle O. Edet
Designation: Partner
Address: QRM Building, 14 Harmony Close, P.O. Box 58314, Victoria Island Lagos, Nigeria
Tel: +234 1 7395162
mobile: +234 1 7061527394
Email: koedet@larkmoorassociates.com
website www.larkmoorassociates.com

```html
<!DOCTYPE html>
<html lang="en">
<head>
<meta charset="utf-8">
<title>Larkmoor Associates – Business Cards</title>
<link href="https://fonts.googleapis.com/css2?family=Quicksand:wght@400;500;700&display=swap" rel="stylesheet">
<style>
  :root {
    --stage: #26272b;
    --card-black: #0d0d0f;
    --pattern-black: #161618;
    --silver-light: #f5f8fc;
    --silver-mid: #d9e1ec;
    --silver-dark: #a7b4c6;
    --ink: #1b1f2a;
    --brand: #c8d3e2;
  }
  * { margin: 0; padding: 0; box-sizing: border-box; }
  html, body {
    width: 1200px; height: 900px; overflow: hidden;
    background: var(--stage);
    font-family: "Quicksand", sans-serif;
  }
  .stage {
    position: relative; width: 1200px; height: 900px;
    display: flex; align-items: center; justify-content: center; gap: 60px;
  }
  .card {
    position: relative; width: 500px; height: 286px;
    background: var(--card-black); overflow: hidden;
    box-shadow: 0 18px 40px rgba(0,0,0,.55);
  }
  /* Front: identity + contact */
  .card-front .silver-band {
    position: absolute; inset: 0; width: 100%; height: 100%;
  }
  .card-front .brand {
    position: absolute; left: 30px; top: 24px;
    display: flex; align-items: center; gap: 14px;
  }
  .brand-mark {
    width: 40px; height: 40px; background: var(--brand);
  }
  .brand-name {
    color: var(--brand); font-weight: 700; line-height: 1;
  }
  .card-front .brand-name { font-size: 24px; }
  .brand-name .sub { display: block; font-size: .62em; text-align: right; }
  .person {
    position: absolute; left: 30px; bottom: 26px; color: var(--ink);
  }
  .person-name { font-size: 19px; font-weight: 500; letter-spacing: .5px; }
  .person-role { font-size: 10px; font-weight: 500; margin-left: 4px; }
  .address { margin-top: 8px; font-size: 11px; line-height: 1.45; font-weight: 500; }
  .contact {
    position: absolute; right: 26px; top: 84px; color: var(--ink);
    font-size: 11px; line-height: 1.75; font-weight: 500; list-style: none;
  }
  .contact b { font-weight: 500; margin-right: 4px; }

  /* Back: brand face */
  .card-back .pattern-fill {
    position: absolute; inset: 0; background: var(--pattern-black);
  }
  .card-back .brand {
    position: absolute; left: 0; right: 0; top: 82px;
    display: flex; flex-direction: column; align-items: center; gap: 14px;
  }
  .card-back .brand-mark { width: 50px; height: 50px; }
  .card-back .brand-name { font-size: 40px; }
  .card-back .brand-name .sub { font-size: .6em; }
  .web {
    position: absolute; left: 0; right: 0; bottom: 34px; text-align: center;
    color: var(--brand); font-size: 12px; letter-spacing: 3px; font-weight: 500;
  }
</style>
</head>
<body>
<main class="stage">
  <section class="card card-front">
    <svg class="silver-band" viewBox="0 0 500 286" preserveAspectRatio="none" aria-hidden="true">
      <defs>
        <linearGradient id="silver" x1="0" y1="0" x2="1" y2="1">
          <stop offset="0" stop-color="#a7b4c6"/>
          <stop offset=".45" stop-color="#f5f8fc"/>
          <stop offset="1" stop-color="#d9e1ec"/>
        </linearGradient>
      </defs>
      <polygon points="0,165 500,20 500,286 0,286" fill="url(#silver)"/>
    </svg>
    <div class="brand">
      <span class="brand-mark"></span>
      <span class="brand-name">Larkmoor<span class="sub">Associates</span></span>
    </div>
    <div class="person">
      <p><span class="person-name">Kunle O. Edet</span><span class="person-role">Partner</span></p>
      <p class="address">QRM Building, 14 Harmony Close,<br>P.O. Box 58314, Victoria Island Lagos,<br>Nigeria</p>
    </div>
    <ul class="contact">
      <li><b>t:</b>+234 1 7395162</li>
      <li><b>m:</b>+234 1 7061527394</li>
      <li><b>e:</b>koedet@larkmoorassociates.com</li>
      <li><b>w:</b>www.larkmoorassociates.com</li>
    </ul>
  </section>

  <section class="card card-back">
    <div class="pattern-fill" role="img" aria-label="Faint repeating brand-mark pattern across the card background"></div>
    <div class="brand">
      <span class="brand-mark"></span>
      <span class="brand-name">Larkmoor<span class="sub">Associates</span></span>
    </div>
    <p class="web">www.larkmoorassociates.com</p>
  </section>
</main>
</body>
</html>
```